Design a Bold Tradeshow Backdrop for a Sustainable Cleaning Technology

We need a professional, high-impact 10' × 8' tradeshow backdrop for Vornelle®, a commercial cleaning technology company. 143.75" x 90" high and needs bleeds in the 143.75" direction for printing but the graphic area is 10' wide.

Our first event will have an audience that includes K–12 school administrators, facility managers, business officials, and custodial decision-makers. However, this backdrop will be used at multiple future trade shows across different commercial and institutional markets.

The design therefore needs to be universal rather than specifically education- or school-themed.

Our goal is to stop attendees as they walk past the booth and immediately communicate a simple message:

Safer and more sustainable cleaning can also cost substantially less than conventional cleaning chemicals.

We want the design to feel modern, innovative, clean, sustainable, credible, commercial, and premium. It should resonate with K–12 decision-makers while being equally appropriate at events serving commercial facilities, healthcare, hospitality, government, property management, transportation, and other institutional markets.

It should NOT look like a traditional janitorial supply advertisement and should not be overly busy.

The most important messages need to be understandable from approximately 10–20 feet away.

Required Messaging

The primary headline should be:

SUSTAINABLE CLEANING
DOES NOT HAVE TO BE EXPENSIVE.

Three major value propositions should be prominently displayed:

FREE
Cleaning Chemical Analysis
See how much you can save.

SAVE UP TO 60% or More
on Cleaning Chemical Costs

AS LITTLE AS $0.27/GALLON

We would also like a strong secondary message incorporated into the design:

SMARTER CLEANING.
High Performance. Low Cost. Safer.

Visual Direction — Important

Rather than showing a K–12 school hallway or other environment that limits the backdrop to the education market, we want a sophisticated, universal commercial or institutional environment.

This could be a bright, contemporary commercial facility, lobby, corridor, office environment, public building, or other premium architectural space that could reasonably represent many different types of facilities.

The environment should communicate:

Cleanliness • Safety • Sustainability • Professionalism • Efficiency • High Performance

We want someone from a school, hospital, hotel, office building, airport, government facility, or other commercial property to be able to look at the backdrop and relate the imagery to their own facility.

Please avoid imagery that makes the backdrop industry-specific.

We also want to avoid clichéd environmental imagery. The design does not need to be covered in leaves, trees, water droplets, recycling symbols, or other obvious "green" graphics to communicate sustainability. We prefer a sophisticated commercial interpretation of sustainability.

Color & Brand Direction

We want the overall color palette to stay primarily within:

Blues — consistent with our corporate identity

Greens — to reinforce sustainability, safety, efficiency, and environmental responsibility

White — strongly encouraged for clean space, contrast, and an open contemporary appearance

Black — should be limited primarily to text where necessary for readability

Please avoid making black a major background or dominant design color.

We want the finished display to have a bright, clean, sophisticated, sustainable look and feel rather than a dark or industrial appearance.

The design should use significant negative space and a strong visual hierarchy.

Less is more.

We prefer a few large, powerful messages that can be understood quickly rather than numerous small bullet points, paragraphs, or icons.

Creative Freedom

The attached concept image is provided to communicate our general direction and messaging only.

It does not need to be copied.

We are specifically running this contest because we want designers to improve upon our initial concept and show us different creative approaches to presenting the Vornelle value proposition.

We are open to creative interpretations of the commercial environment, composition, typography, use of negative space, and how the three major financial benefits are presented.

The finished design should feel like an innovative commercial technology brand, not simply another cleaning chemical company.

Corporate Logo — Very Important

We are attaching our official Vornelle® corporate logo for use in the design.

DO NOT redraw, recreate, modify, stylize, reinterpret, trace, or AI-generate the Vornelle logo.

The supplied corporate logo must be inserted directly into the artwork exactly as provided, maintaining its original proportions, colors, typography, trademark elements, and graphic design.

The logo should generally appear in the upper-left area of the backdrop but should not overwhelm the primary marketing message.

Printer Template & Graphic Sizing

We are also attaching the printer's official graphic template and instructions for the 8' × 8' tension-fabric display.

Designers should create their artwork using these supplied specifications so the winning design can be transferred directly into production.

The printer requires that the original document size not be changed, artwork be created on the designated design layer or a new layer, images be embedded, text be converted to outlines, and the finished production artwork be supplied as a PDF.

Please pay particular attention to the bleed area, finished size, and safe artwork area when positioning important text, graphics, and the corporate logo.

Physical Booth Context

The backdrop will sit behind an 8' tradeshow table.

The complete booth will also contain:

A blue stretch tablecloth with the Vornelle corporate logo
BrevoMax and Vornelle product containers and samples on the table
An HulaDrent chemical mixing/dilution station displayed on an elevated stand to the left
A television/monitor to the right demonstrating our online ROI cost-savings calculator

Because these other booth elements will explain our products and technology in greater detail, the backdrop should NOT attempt to explain everything we do.

Its primary purpose is to stop traffic, establish the Vornelle brand, and communicate our core economic and sustainability value proposition.

Final Deliverables

The winning designer must provide artwork properly sized and positioned using our supplied 8' × 8' tension-fabric display template.

Final files should include:

Print-ready, high-resolution PDF
Editable source/vector artwork
All images embedded
Fonts converted to outlines
Artwork correctly positioned within the supplied printer template
Original Vornelle corporate logo incorporated without modification
The 3–5 Second Test

This is perhaps the most important requirement.

Someone walking down a tradeshow aisle should be able to look at the backdrop for 3–5 seconds and understand:

Vornelle offers safer, sustainable, high-performance commercial cleaning — at a lower cost.

The three offers we particularly want them to remember are:

FREE CHEMICAL ANALYSIS

SAVE UP TO 60%

AS LITTLE AS $0.27/GALLON

The overall takeaway should be:

Sustainable cleaning does not have to cost more.

We want the winning design to make that message immediately understandable, credible, and memorable.

Colors
0054AA
0677BA
7BADD7
CADEEF
E8F1F8
0094D4
00A9DD
6FCCEA
C7EBF8
E9F6FB
00AB8E
00BBA5
67D7C9
C6EFE9
E9F9F6
59FF00
82FF00
B8FF75
E3FFCB
F4FFEA

```html
<!DOCTYPE html>
<html lang="en">
<head>
<meta charset="utf-8">
<title>Vornelle – Sustainable Cleaning Backdrop</title>
<link rel="stylesheet" href="https://fonts.googleapis.com/css2?family=Poppins:wght@400;500;600;700;800&display=swap">
<style>
:root{
  --navy:#1a3768;
  --navy-deep:#0f1f5e;
  --green:#6aa63c;
  --green-bright:#8cc652;
  --ink:#1b1b1b;
  --white:#ffffff;
  --marble-light:#f4ece2;
  --marble-mid:#d8c4ad;
  --marble-warm:#b89a7c;
}
*{margin:0;padding:0;box-sizing:border-box}
html,body{width:1200px;height:1200px;overflow:hidden;background:var(--white)}
.backdrop{position:relative;width:1200px;height:1200px;font-family:'Poppins',sans-serif;background:var(--white);overflow:hidden}
.abs{position:absolute;line-height:1;white-space:nowrap}

.brand{left:0;width:843px;top:100px;text-align:center}
.brand-name{font-weight:700;font-size:78px;color:var(--navy);letter-spacing:-2px}
.brand-tagline{left:0;width:843px;top:224px;text-align:center;font-weight:500;font-size:24px;letter-spacing:3px;color:var(--navy)}

.headline{left:0;width:843px;text-align:center;font-weight:700;font-size:84px;letter-spacing:-1.5px}
.headline.green{color:var(--green)}
.headline.navy{color:var(--navy)}

.step{width:42px;height:42px;border-radius:50%;border:2px solid var(--navy);background:radial-gradient(circle at 35% 35%,var(--green-bright),var(--navy) 80%);color:var(--white);font-weight:700;font-size:24px;display:flex;align-items:center;justify-content:center;line-height:1}
.step-line{height:0;border-top:2px dotted var(--navy)}

.offer{text-align:center}
.offer-divider{width:1px;top:717px;height:170px;background:#e6e6e6;box-shadow:2px 0 6px rgba(0,0,0,.12)}
.offer-big{font-weight:700;color:var(--navy);letter-spacing:-1px}
.offer-small{font-size:18px;line-height:23.5px;color:var(--ink);font-weight:400;white-space:normal}
.save-label{font-weight:700;font-size:21px;line-height:19px;color:var(--navy);text-align:left}
.caps-note{font-size:18px;color:var(--ink);font-weight:400}

.facility-photo{left:831px;top:0;width:369px;height:902px;background:linear-gradient(180deg,var(--marble-light) 0%,#e9dccb 30%,#f6f1ea 48%,var(--marble-mid) 70%,var(--marble-warm) 100%)}

.values-band{left:0;top:916px;width:828px;height:284px;background:linear-gradient(90deg,var(--navy-deep) 0%,#274a6a 40%,#5e8a6b 75%,var(--green-bright) 100%)}
.values-divider{left:380px;top:974px;width:1px;height:171px;background:rgba(255,255,255,.55)}
.value{display:flex;align-items:center;gap:12px;color:var(--white);font-weight:700;font-size:31px}
.value svg{width:25px;height:25px;flex:none}

.smarter-block{left:828px;top:916px;width:372px;height:284px;background:linear-gradient(135deg,#1a3a8a 0%,var(--navy-deep) 100%)}
.smarter-title{left:872px;font-weight:700;font-size:58px;color:var(--white);letter-spacing:-.5px}
.smarter-line{left:882px;font-size:21px;color:var(--white);font-weight:400}
</style>
</head>
<body>
<main class="backdrop">

  <div class="abs brand"><span class="brand-name">Vornelle®</span></div>
  <div class="abs brand-tagline">SURFACE CARE SYSTEMS</div>

  <div class="abs headline green" style="top:299px">SUSTAINABLE</div>
  <div class="abs headline navy" style="top:374px">CLEANING</div>
  <div class="abs headline green" style="top:450px">DOES NOT HAVE</div>
  <div class="abs headline navy" style="top:526px">TO BE EXPENSIVE.</div>

  <div class="abs step" style="left:137px;top:664px">1</div>
  <div class="abs step-line" style="left:194px;top:685px;width:218px"></div>
  <div class="abs step" style="left:427px;top:664px">2</div>
  <div class="abs step-line" style="left:485px;top:685px;width:205px"></div>
  <div class="abs step" style="left:699px;top:664px">3</div>

  <div class="abs offer-divider" style="left:308px"></div>
  <div class="abs offer-divider" style="left:599px"></div>

  <div class="abs offer" style="left:12px;width:300px;top:733px">
    <div class="offer-big" style="font-size:64px">FREE</div>
    <div class="offer-small" style="margin-top:8px">Cleaning Chemical<br>Analysis See how<br>much you can save.</div>
  </div>

  <div class="abs offer" style="left:314px;width:280px;top:734px">
    <div style="display:inline-flex;align-items:center;gap:8px">
      <div class="save-label">SAVE<br>UP TO</div>
      <div class="offer-big" style="font-size:64px">60%</div>
    </div>
    <div class="offer-small" style="margin-top:6px">or More on Cleaning<br>Chemical Costs</div>
  </div>

  <div class="abs offer" style="left:603px;width:240px;top:741px">
    <div class="caps-note">AS LITTLE AS</div>
    <div class="offer-big" style="font-size:66px;margin-top:8px"><span style="font-size:34px;vertical-align:22px">$</span>0.27</div>
    <div class="caps-note" style="margin-top:10px">/GALLON</div>
  </div>

  <div class="abs facility-photo" role="img" aria-label="Bright modern lobby with glossy marble floor, columns, potted plants and tall windows"></div>

  <div class="abs values-band"></div>
  <div class="abs values-divider"></div>

  <svg width="0" height="0" style="position:absolute">
    <symbol id="tick" viewBox="0 0 24 24"><circle cx="12" cy="12" r="12" fill="#fff"/><path d="M6.5 12.5l3.5 3.5 7.5-8" fill="none" stroke="#1e3a6a" stroke-width="3" stroke-linecap="round" stroke-linejoin="round"/></symbol>
  </svg>

  <div class="abs value" style="left:76px;top:990px"><svg><use href="#tick"/></svg>Cleanliness</div>
  <div class="abs value" style="left:76px;top:1044px"><svg><use href="#tick"/></svg>Safety</div>
  <div class="abs value" style="left:76px;top:1099px"><svg><use href="#tick"/></svg>Sustainability</div>
  <div class="abs value" style="left:421px;top:989px"><svg><use href="#tick"/></svg>Professionalism</div>
  <div class="abs value" style="left:421px;top:1043px"><svg><use href="#tick"/></svg>Efficiency</div>
  <div class="abs value" style="left:421px;top:1098px"><svg><use href="#tick"/></svg>High Performance</div>

  <div class="abs smarter-block"></div>
  <div class="abs smarter-title" style="top:939px">SMARTER</div>
  <div class="abs smarter-title" style="top:990px">CLEANING</div>
  <div class="abs smarter-line" style="top:1072px">High Performance.</div>
  <div class="abs smarter-line" style="top:1106px">Low Cost.</div>
  <div class="abs smarter-line" style="top:1140px">Safer.</div>

</main>
</body>
</html>
```